Design Android App for Creating Estimates and Invoices

This project is to create a graphic design for an Android mobile app called Velmira Builder App which is an app that will help contractors to quickly create professional estimates and invoices, accept payments, manage clients and projects and run their business smoothly.

Link to some designs I created myself, hoping to get even better design from you
https://snapvault.example/album/qTrWpe

This project is similar to
https://appmarket.example/store/apps/details?id=com.brevlo.android.brevlo
https://appmarket.example/store/apps/details?id=com.tuvrq.quikbill

Check this Google Doc for more information. http://shrtn.example/8KmPqX4

Target Market(s)

Contractors, Home Improvement Professionals, Home Builders,

Industry/Entity Type

Residential Construction

Requirements
Must have
• Non-cluttered screen for Estimates, Enough white space between fields.
Nice to have
• Be different from the two example designs shown

```html
<!DOCTYPE html>
<html lang="en">
<head>
<meta charset="utf-8">
<title>Velmira Builder App – Screens</title>
<link href="https://fonts.googleapis.com/css2?family=Poppins:wght@400;500;600&display=swap" rel="stylesheet">
<style>
:root{
  --bg:#fee9d8;
  --orange:#ff7a0c;
  --orange-status:#f5821f;
  --orange-light:#ff8b28;
  --orange-active:#ff9a45;
  --white:#ffffff;
  --ink:#2c2f3a;
  --muted:#9a9ca6;
  --line:#ececef;
  --filter:#e8edf4;
  --icon:#6b7cb0;
  --nav-icon:#9ea1aa;
  --saved:#3b5bb5;
  --sent:#7cc243;
  --viewed:#ff7a0c;
  --accepted:#2eaa4a;
  --rejected:#e8453c;
  --scrim:#b4b4b4;
  --scrim-head:#b8733a;
}
*{margin:0;padding:0;box-sizing:border-box}
html,body{width:1200px;height:727px;overflow:hidden}
body{background:var(--bg);font-family:"Poppins",sans-serif;color:var(--ink);position:relative}
.phone{position:absolute;top:127px;width:196px;height:392px;background:var(--white);overflow:hidden}
.phone--estimates{left:79px}
.phone--invoices{left:346px}
.phone--clients{left:612px}
.phone--menu{left:879px;background:var(--scrim)}
.status-bar{height:10px;background:var(--orange-status);display:flex;justify-content:flex-end;align-items:center;gap:3px;padding-right:11px;color:var(--white);font-size:6px;font-weight:500}
.status-bar svg{width:7px;height:6px;fill:var(--white)}
.app-bar{height:40px;background:var(--orange);display:flex;align-items:center;justify-content:space-between;padding:0 11px 0 11.5px}
.app-bar h1{color:var(--white);font-size:11.5px;font-weight:600;letter-spacing:.1px}
.app-bar svg{width:10px;height:10px;stroke:var(--white);fill:none;stroke-width:1.4}
.filter-bar{height:12px;background:var(--filter);display:flex;align-items:center;justify-content:space-between;padding:0 11.5px;font-size:4.6px;color:var(--ink)}
.filter-bar.end{justify-content:flex-end}
.filter-bar span::after{content:"";display:inline-block;margin-left:2px;border:1.3px solid transparent;border-top:1.6px solid var(--ink);vertical-align:0}
.filter-bar .total::after{display:none}
.list{list-style:none;margin:0 11.5px}
.row{display:flex;align-items:center;border-bottom:0.6px solid var(--line)}
.list--estimates .row{height:29.6px}
.list--invoices .row{height:33.9px}
.list--clients .row{height:33.9px}
.avatar{flex:none;width:20px;height:20px;border-radius:50%;margin-right:6.5px}
.list--clients .avatar{margin-right:6.5px}
.av-1{background:radial-gradient(circle at 50% 40%,#d9cfc7,#3a3a3a 70%)}
.av-2{background:radial-gradient(circle at 50% 45%,#6d5446,#1e2733 70%)}
.av-3{background:radial-gradient(circle at 50% 40%,#e9d6b8,#b9c6cf 75%)}
.av-4{background:radial-gradient(circle at 50% 40%,#c9c4c0,#2a2a2a 70%)}
.av-5{background:radial-gradient(circle at 50% 45%,#c58f73,#5b4438 75%)}
.av-6{background:radial-gradient(circle at 50% 40%,#e2c8ab,#8f9a8c 75%)}
.info{flex:1;min-width:0}
.name{font-size:6px;font-weight:500;line-height:1.3}
.meta{font-size:4.4px;color:var(--muted);line-height:1.5}
.amount{text-align:right}
.price{font-size:6px;font-weight:500;line-height:1.3}
.state{font-size:4.6px;line-height:1.5}
.state::before{content:"• "}
.s-saved{color:var(--saved)} .s-sent{color:var(--sent)} .s-viewed{color:var(--viewed)}
.s-accepted{color:var(--accepted)} .s-muted{color:var(--muted)} .s-rejected{color:var(--rejected)}
.actions{display:flex;gap:9px;justify-content:flex-end}
.action{display:flex;flex-direction:column;align-items:center;font-size:3.6px;color:var(--icon);width:10px}
.action svg{width:8px;height:8px;stroke:var(--icon);fill:none;stroke-width:.8;margin-bottom:1px}
.fab{position:absolute;left:156.5px;top:313.5px;width:27px;height:27px;border-radius:50%;background:var(--orange);box-shadow:0 2px 5px rgba(255,122,12,.35);display:flex;align-items:center;justify-content:center}
.fab svg{width:8px;height:8px;stroke:var(--white);stroke-width:1.1}
.bottom-nav{position:absolute;left:0;right:0;bottom:0;height:41px;border-top:0.6px solid var(--line);display:flex;justify-content:space-around;padding:0 14px;align-items:center}
.tab{display:flex;flex-direction:column;align-items:center;gap:3px;font-size:3.9px;color:var(--nav-icon);letter-spacing:.1px;width:30px}
.tab svg{width:12px;height:12px;stroke:var(--nav-icon);fill:none;stroke-width:.7}
.tab.active{color:var(--orange)}
.tab.active svg{stroke:var(--orange)}
/* drawer screen */
.scrim-head{position:absolute;left:0;right:0;top:0;height:50px;background:var(--scrim-head)}
.scrim-status{position:absolute;right:10px;top:2px;color:#e6d2c0;font-size:6px;font-weight:500;display:flex;gap:3px;align-items:center}
.scrim-status svg{width:7px;height:6px;fill:#e6d2c0}
.scrim-search{position:absolute;right:12px;top:28px;width:10px;height:10px;stroke:#e6d2c0;fill:none;stroke-width:1.4}
.scrim-rows{position:absolute;right:0;top:50px;width:44px}
.scrim-row{height:33.9px;border-bottom:0.6px solid #a9a9a9;display:flex;justify-content:flex-end;align-items:center;gap:9px;padding-right:10px}
.scrim-row .action{color:#7c839c}
.scrim-row .action svg{stroke:#7c839c}
.scrim-fab{position:absolute;right:11px;top:313.5px;width:27px;height:27px;border-radius:50%;background:#b36d33;display:flex;align-items:center;justify-content:center}
.scrim-fab svg{width:8px;height:8px;stroke:#d9c6b6;stroke-width:1.1}
.scrim-more{position:absolute;right:24px;bottom:11px;display:flex;flex-direction:column;align-items:center;gap:3px;font-size:3.9px;color:#b86a2e}
.scrim-more svg{width:12px;height:12px;stroke:#b86a2e;fill:none;stroke-width:.7}
.scrim-nav-line{position:absolute;right:0;bottom:41px;width:44px;border-top:0.6px solid #a9a9a9}
.drawer{position:absolute;left:0;top:0;bottom:0;width:152px;background:var(--orange)}
.drawer-profile{height:96px;background:var(--orange-light);display:flex;flex-direction:column;align-items:center;padding-top:15px}
.profile-photo{width:46px;height:46px;border-radius:50%;background:radial-gradient(circle at 50% 42%,#a47d66,#1f242c 68%)}
.profile-name{color:var(--white);font-size:6.6px;font-weight:500;margin-top:6px;line-height:1.2}
.profile-phone{color:var(--white);font-size:5px;line-height:1.5}
.menu{list-style:none;margin-top:4px}
.menu li{height:18.3px;display:flex;align-items:center;padding-left:10px;color:var(--white);font-size:5.6px;gap:11px}
.menu li svg{width:9px;height:9px;stroke:#ffd0a8;fill:none;stroke-width:.7}
.menu li.active{background:var(--orange-active);font-weight:600}
.sign-out{position:absolute;left:40.5px;top:336px;width:69.5px;height:17px;background:var(--white);border-radius:1px;display:flex;align-items:center;justify-content:center;color:var(--orange);font-size:6.4px;font-weight:500}
.version{position:absolute;left:0;right:0;bottom:0;height:17.5px;background:var(--orange-light);display:flex;align-items:center;justify-content:center;color:var(--white);font-size:5.4px;font-weight:500}
</style>
</head>
<body>

<svg width="0" height="0" style="position:absolute" aria-hidden="true">
  <defs>
    <symbol id="i-search" viewBox="0 0 20 20"><circle cx="9" cy="9" r="7"/><path d="M14 14l4.5 4.5"/></symbol>
    <symbol id="i-wifi" viewBox="0 0 14 12"><path d="M0 1.5Q7-2 14 1.5L7 12z"/></symbol>
    <symbol id="i-signal" viewBox="0 0 12 12"><path d="M12 0v12H0z"/></symbol>
    <symbol id="i-battery" viewBox="0 0 8 12"><rect x="1.5" y="1" width="5" height="11" rx=".5"/><rect x="3" y="0" width="2" height="1"/></symbol>
    <symbol id="i-plus" viewBox="0 0 16 16"><path d="M8 1v14M1 8h14"/></symbol>
    <symbol id="i-call" viewBox="0 0 16 16"><path d="M4 1.5l2.3 3-1.6 1.6a9 9 0 005.2 5.2l1.6-1.6 3 2.3-1.6 2.3C7 14 2 9 1.7 3.1z"/><path d="M9.5 2.5a4 4 0 014 4M9.5 5a1.6 1.6 0 011.6 1.6"/></symbol>
    <symbol id="i-email" viewBox="0 0 16 16"><path d="M1.5 6.5L8 1.5l6.5 5V15h-13z"/><path d="M1.5 6.5L8 11l6.5-4.5"/><path d="M4 5V3.5h8V5"/><path d="M1.5 15l5-4.3M14.5 15l-5-4.3"/></symbol>
    <symbol id="i-sms" viewBox="0 0 16 16"><rect x="1" y="3" width="14" height="10" rx=".5"/><path d="M1 3.5l7 5.5 7-5.5"/></symbol>
    <symbol id="i-pie" viewBox="0 0 20 20"><path d="M9 3.5a7.5 7.5 0 107.5 7.5H9z"/><path d="M11 1.5a7.5 7.5 0 017.5 7.5H11z"/></symbol>
    <symbol id="i-doc" viewBox="0 0 20 20"><rect x="4" y="1.5" width="12" height="17"/><path d="M7 5h6M7 8h6M7 11h6M7 14h4"/></symbol>
    <symbol id="i-people" viewBox="0 0 20 20"><circle cx="7.5" cy="6" r="3"/><path d="M2 17l1.5-5.5a4.2 4.2 0 018 0L13 17"/><circle cx="13" cy="5" r="2.6"/><path d="M12.5 9.2a3.8 3.8 0 014.5 2.3L18.5 16"/></symbol>
    <symbol id="i-grid" viewBox="0 0 20 20"><circle cx="3.5" cy="3.5" r="1.5"/><circle cx="10" cy="3.5" r="1.5"/><circle cx="16.5" cy="3.5" r="1.5"/><circle cx="3.5" cy="10" r="1.5"/><circle cx="10" cy="10" r="1.5"/><circle cx="16.5" cy="10" r="1.5"/><circle cx="3.5" cy="16.5" r="1.5"/><circle cx="10" cy="16.5" r="1.5"/><circle cx="16.5" cy="16.5" r="1.5"/></symbol>
    <symbol id="i-list" viewBox="0 0 20 20"><circle cx="3" cy="4" r="1.6"/><circle cx="3" cy="10" r="1.6"/><circle cx="3" cy="16" r="1.6"/><path d="M7 4h11M7 10h11M7 16h11"/></symbol>
    <symbol id="i-user" viewBox="0 0 20 20"><circle cx="10" cy="10" r="8.5"/><circle cx="10" cy="8" r="3"/><path d="M4.5 16a6.5 6.5 0 0111 0"/></symbol>
    <symbol id="i-gear" viewBox="0 0 20 20"><circle cx="10" cy="10" r="8.5"/><circle cx="10" cy="10" r="5.5"/><circle cx="10" cy="10" r="2.2"/></symbol>
    <symbol id="i-support" viewBox="0 0 20 20"><circle cx="10" cy="10" r="8.5"/><path d="M5.5 10a4.5 4.5 0 019 0v3h-2v-3M5.5 13v-3h2v3z"/></symbol>
  </defs>
</svg>

<!-- Estimates -->
<section class="phone phone--estimates">
  <div class="status-bar"><svg><use href="#i-wifi"/></svg><svg><use href="#i-signal"/></svg><svg><use href="#i-battery"/></svg>12:30</div>
  <header class="app-bar"><h1>Estimates</h1><svg><use href="#i-search"/></svg></header>
  <div class="filter-bar end"><span>View all</span></div>
  <ul class="list list--estimates">
    <li class="row"><div class="info"><div class="name">Owen Tallis Const.</div><div class="meta">EST0021 · May 6, 2019</div></div><div class="amount"><div class="price">$2512.50</div><div class="state s-saved">Saved</div></div></li>
    <li class="row"><div class="info"><div class="name">Brightway Inc.</div><div class="meta">EST0022 · May 6, 2019</div></div><div class="amount"><div class="price">$1106.00</div><div class="state s-sent">Sent</div></div></li>
    <li class="row"><div class="info"><div class="name">Okafor and Sons LTD.</div><div class="meta">EST0026 · May 8, 2019</div></div><div class="amount"><div class="price">$4500.00</div><div class="state s-viewed">Viewed</div></div></li>
    <li class="row"><div class="info"><div class="name">Owen Tallis Const.</div><div class="meta">EST0033 · May 12, 2019</div></div><div class="amount"><div class="price">$2512.50</div><div class="state s-accepted">Accepted</div></div></li>
    <li class="row"><div class="info"><div class="name">Brightway Inc.</div><div class="meta">EST0062 · June 2, 2019</div></div><div class="amount"><div class="price">$1106.00</div><div class="state s-muted">Expired</div></div></li>
    <li class="row"><div class="info"><div class="name">Okafor and Sons LTD.</div><div class="meta">EST0076 · June 8, 2019</div></div><div class="amount"><div class="price">$4500.00</div><div class="state s-rejected">Rejected</div></div></li>
  </ul>
  <div class="fab"><svg><use href="#i-plus"/></svg></div>
  <nav class="bottom-nav">
    <div class="tab active"><svg><use href="#i-pie"/></svg>ESTIMATES</div>
    <div class="tab"><svg><use href="#i-doc"/></svg>INVOICES</div>
    <div class="tab"><svg><use href="#i-people"/></svg>CLIENTS</div>
    <div class="tab"><svg><use href="#i-grid"/></svg>MORE</div>
  </nav>
</section>

<!-- Invoices -->
<section class="phone phone--invoices">
  <div class="status-bar"><svg><use href="#i-wifi"/></svg><svg><use href="#i-signal"/></svg><svg><use href="#i-battery"/></svg>12:30</div>
  <header class="app-bar"><h1>Invoices</h1><svg><use href="#i-search"/></svg></header>
  <div class="filter-bar"><span>View all</span><span class="total">$22,345.34</span></div>
  <ul class="list list--invoices">
    <li class="row"><div class="avatar av-1" role="img" aria-label="Client photo"></div><div class="info"><div class="name">Owen Tallis</div><div class="meta">INV0021 · May 6, 2019</div></div><div class="amount"><div class="price">$2512.50</div><div class="state s-sent">Sent</div></div></li>
    <li class="row"><div class="avatar av-2" role="img" aria-label="Client photo"></div><div class="info"><div class="name">Reid Palmer</div><div class="meta">INV0022 · May 6, 2019</div></div><div class="amount"><div class="price">$1039.00</div><div class="state s-saved">Draft</div></div></li>
    <li class="row"><div class="avatar av-3" role="img" aria-label="Client photo"></div><div class="info"><div class="name">Nora Ellwyn</div><div class="meta">INV0026 · May 8, 2019</div></div><div class="amount"><div class="price">$4500.00</div><div class="state s-muted">Written Off</div></div></li>
    <li class="row"><div class="avatar av-4" role="img" aria-label="Client photo"></div><div class="info"><div class="name">Dario Keyes</div><div class="meta">INV0122 · May 6, 2019</div></div><div class="amount"><div class="price">$2512.50</div><div class="state s-viewed">Void</div></div></li>
    <li class="row"><div class="avatar av-5" role="img" aria-label="Client photo"></div><div class="info"><div class="name">Milo Harte</div><div class="meta">INV0234 · May 6, 2019</div></div><div class="amount"><div class="price">$1039.00</div><div class="state s-accepted">Paid</div></div></li>
    <li class="row"><div class="avatar av-6" role="img" aria-label="Client photo"></div><div class="info"><div class="name">Ivy Lorne</div><div class="meta">INV0026 · May 8, 2019</div></div><div class="amount"><div class="price">$4500.00</div><div class="state s-rejected">Overdue</div></div></li>
  </ul>
  <div class="fab"><svg><use href="#i-plus"/></svg></div>
  <nav class="bottom-nav">
    <div class="tab"><svg><use href="#i-pie"/></svg>ESTIMATES</div>
    <div class="tab active"><svg><use href="#i-doc"/></svg>INVOICES</div>
    <div class="tab"><svg><use href="#i-people"/></svg>CLIENTS</div>
    <div class="tab"><svg><use href="#i-grid"/></svg>MORE</div>
  </nav>
</section>

<!-- Clients -->
<section class="phone phone--clients">
  <div class="status-bar"><svg><use href="#i-wifi"/></svg><svg><use href="#i-signal"/></svg><svg><use href="#i-battery"/></svg>12:30</div>
  <header class="app-bar"><h1>Clients</h1><svg><use href="#i-search"/></svg></header>
  <ul class="list list--clients">
    <li class="row"><div class="avatar av-1" role="img" aria-label="Client photo"></div><div class="info"><div class="name">Owen Tallis</div><div class="meta">Austin, TX</div></div>
      <div class="actions"><div class="action"><svg><use href="#i-call"/></svg>Call</div><div class="action"><svg><use href="#i-email"/></svg>Email</div><div class="action"><svg><use href="#i-sms"/></svg>SMS</div></div></li>
    <li class="row"><div class="avatar av-2" role="img" aria-label="Client photo"></div><div class="info"><div class="name">Reid Palmer</div><div class="meta">Charlotte, NC</div></div>
      <div class="actions"><div class="action"><svg><use href="#i-call"/></svg>Call</div><div class="action"><svg><use href="#i-sms"/></svg>SMS</div></div></li>
    <li class="row"><div class="avatar av-3" role="img" aria-label="Client photo"></div><div class="info"><div class="name">Nora Ellwyn</div><div class="meta">Portland, ME</div></div>
      <div class="actions"><div class="action"><svg><use href="#i-email"/></svg>Email</div><div class="action"><svg><use href="#i-sms"/></svg>SMS</div></div></li>
    <li class="row"><div class="avatar av-4" role="img" aria-label="Client photo"></div><div class="info"><div class="name">Dario Keyes</div><div class="meta">Birmingham, AL</div></div>
      <div class="actions"><div class="action"><svg><use href="#i-call"/></svg>Call</div></div></li>
    <li class="row"><div class="avatar av-5" role="img" aria-label="Client photo"></div><div class="info"><div class="name">Milo Harte</div><div class="meta">Seattle, WA</div></div>
      <div class="actions"><div class="action"><svg><use href="#i-call"/></svg>Call</div><div class="action"><svg><use href="#i-email"/></svg>Email</div></div></li>
    <li class="row"><div class="avatar av-6" role="img" aria-label="Client photo"></div><div class="info"><div class="name">Ivy Lorne</div><div class="meta">Los Angeles, CA</div></div>
      <div class="actions"><div class="action"><svg><use href="#i-call"/></svg>Call</div><div class="action"><svg><use href="#i-email"/></svg>Email</div><div class="action"><svg><use href="#i-sms"/></svg>SMS</div></div></li>
  </ul>
  <div class="fab"><svg><use href="#i-plus"/></svg></div>
  <nav class="bottom-nav">
    <div class="tab"><svg><use href="#i-pie"/></svg>ESTIMATES</div>
    <div class="tab"><svg><use href="#i-doc"/></svg>INVOICES</div>
    <div class="tab active"><svg><use href="#i-people"/></svg>CLIENTS</div>
    <div class="tab"><svg><use href="#i-grid"/></svg>MORE</div>
  </nav>
</section>

<!-- Navigation drawer -->
<section class="phone phone--menu">
  <div class="scrim-head"></div>
  <div class="scrim-status"><svg><use href="#i-signal"/></svg><svg><use href="#i-battery"/></svg>12:30</div>
  <svg class="scrim-search"><use href="#i-search"/></svg>
  <div class="scrim-rows">
    <div class="scrim-row"><div class="action"><svg><use href="#i-email"/></svg>Email</div><div class="action"><svg><use href="#i-sms"/></svg>SMS</div></div>
    <div class="scrim-row"><div class="action"><svg><use href="#i-call"/></svg>Call</div><div class="action"><svg><use href="#i-sms"/></svg>SMS</div></div>
    <div class="scrim-row"><div class="action"><svg><use href="#i-email"/></svg>Email</div><div class="action"><svg><use href="#i-sms"/></svg>SMS</div></div>
    <div class="scrim-row"><div class="action"><svg><use href="#i-call"/></svg>Call</div></div>
    <div class="scrim-row"><div class="action"><svg><use href="#i-call"/></svg>Call</div><div class="action"><svg><use href="#i-email"/></svg>Email</div></div>
    <div class="scrim-row"><div class="action"><svg><use href="#i-email"/></svg>Email</div><div class="action"><svg><use href="#i-sms"/></svg>SMS</div></div>
  </div>
  <div class="scrim-fab"><svg><use href="#i-plus"/></svg></div>
  <div class="scrim-nav-line"></div>
  <div class="scrim-more"><svg><use href="#i-grid"/></svg>MORE</div>

  <aside class="drawer">
    <div class="drawer-profile">
      <div class="profile-photo" role="img" aria-label="Account holder profile photo"></div>
      <div class="profile-name">Caleb Strand</div>
      <div class="profile-phone">+100 555 0142</div>
    </div>
    <ul class="menu">
      <li><svg><use href="#i-pie"/></svg>Estimates</li>
      <li><svg><use href="#i-doc"/></svg>Invoices</li>
      <li class="active"><svg><use href="#i-people"/></svg>Clients</li>
      <li><svg><use href="#i-list"/></svg>Items</li>
      <li><svg><use href="#i-user"/></svg>My Account</li>
      <li><svg><use href="#i-gear"/></svg>Settings</li>
      <li><svg><use href="#i-support"/></svg>Support</li>
    </ul>
    <div class="sign-out">Sign Out</div>
    <div class="version">v 0.0.1</div>
  </aside>
</section>

</body>
</html>
```